Flyer Design for International Business Consultant

We need an advertisement to help build the profile of Colin Marsh, Senior Consultant and Director at 'LUPE Advisory Group'.

What we want to promote:
Our Senior Consultant and Director, Colin Marsh as expert on all matters China related.

Who are we promoting to:
Industry associations and networking groups.

Why:
Many organisations are interested in reaching the Chinese market, however don't know who to go to or who to trust. With many consultants out there trying to claim they offer a similar service, LUPE would like to promote Colin as a genuine expert in the field and the 'go to' person on all things China business related. To do this, we are in the process of building Colin's national and international profile, which includes advertising Colin expertise to industry associations and networking groups so that they consider booking Colin as a key note speaker at conferences. We know that our target audience are more inclined to seek the advice of someone they have seen speak at a conference than to find someone in the Blue listings or via findly search.

A Bit about Colin Marsh:

Colin Marsh has lived, worked and studied in China for extended periods, speaks and writes fluently in Chinese, was formerly a Member of the Regional Trade Outreach Steering Panel, is a member of the Institute of Cross-Border Commerce and is a member of the Pacific Trade Partners Forum to name a few. To add to his credentials, Colin has by invitation lectured for 5 consecutive years in Management and Economics at Masters Level to students at Harbourline Institute.

Colin’s qualifications include: Bachelor of Arts (Asian Studies), Bachelor of Business (Applied Economics – International Trade), Master of Business in Applied Economics (International Business) and currently completing a Doctor of Business Administration (International Business Management) which has an economics focus and researches the export of Australian professional services to China.

Colin has been the Principal Consultant for a number of LUPE’s clients including the recent assignment commissioned by Victorian based company Bremo Freight, who have benefited from a $40 million deal with Eastern Iron Works (EIW). This project has also resulted in EIW, China’s largest train manufacturer decision to set up offices in Victoria.

Colin is an expert in Australia/China Business relations and has been paramount to the success of numerous international business transactions. As mentioned, Colin is not only fluent in spoken and written Mandarin, but is also a bi-cultural expert (meaning he knows both Australian and Chinese) cultures. From Australian and Chinese history, art, food and more, Colin Marsh provides his clients with more than translation services.

A Bit about LUPE Advisory Group:

Run by experienced business executives with over 20 years’ experience in the Chinese and Australian markets, LUPE brings a un-paralleled level of knowledge and expertise that enables cooperative business relations to develop between international organisations despite the language and cultural differences. They are a bi-lingual and bi-cultural international business consultancy that specialise in managing cross-border business involving China.

LUPE has expertise in all facets of business management and has worked with a range of companies and organisations to develop and implement strategic business solutions to set direction, improve performance and maximise returns to stakeholders. LUPE has particular expertise in economic and market analysis and specialises in project management of large and complex projects, strategic procurement, market research and market development strategies. Combined with their cultural and language skills, LUPE provides a unique and high value contribution to international projects.
Updates

Good afternoon designers

Thank you for your submissions so far.  We are happy with some of the designs that have come in, however, many of you have produced flyers that have too much information in it.  We are looking for something more concise that does not appear to be either a copy of information I have posted in this brief or a fancy looking resume for Colin Marsh. 

Please remember, we are communicating to event co-ordinators who are looking to appoint guest speakers at an upcoming conference.  They want someone who is going to discuss some of the 'hot topics' their audience are interested in, someone who is experienced in the topic and someone who is interesting. We need to communicate all of this in a concise, and creative way so that we can make Colin Marsh stand out above the rest.

Dear Designers

Thank you all very much for your submissions.  We appreciate you taking the time to compose a flyer for our organisation. 

Regards
Tessa

Dear Designers

Regards
Tessa

Target Market(s)

Event/conference managers or coordinators

Industry/Entity Type

Business Management

Requirements
Must have
• Must have the LUPE Logo on it (red, white and black). The ad will be in the form of an electronic flyer to be embedded in an email that will be sent on to relevant contacts in our database.

```html
<!DOCTYPE html>
<html lang="en">
<head>
<meta charset="utf-8">
<title>LUPE Advisory Group – Colin Marsh</title>
<link rel="stylesheet" href="https://fonts.googleapis.com/css2?family=Oswald:wght@500&family=Source+Sans+3:ital,wght@0,400;0,600;0,700;1,400;1,700&display=swap">
<style>
  :root {
    --red: #e3161b;
    --ink: #1d1d1b;
    --paper: #ffffff;
    --frame: #7a7a7a;
    --figure-dark: #2e2e2e;
    --figure-mid: #6f6f6f;
    --figure-light: #b5b5b5;
  }
  * { box-sizing: border-box; margin: 0; padding: 0; }
  html, body {
    width: 1200px; height: 850px; overflow: hidden;
    background: var(--paper);
  }
  .flyer {
    position: relative; width: 1200px; height: 850px;
    background: var(--paper);
    font-family: "Source Sans 3", "Myriad Pro", sans-serif;
    color: var(--ink);
  }
  .flyer__frame {
    position: absolute; left: 50px; top: 61px; width: 1108px; height: 689px;
    border: 1px solid var(--frame);
    overflow: hidden;
  }
  .crowd-art {
    position: absolute; left: 0; top: 0; width: 520px; height: 689px;
  }
  .tagline {
    position: absolute; left: 14px; width: 480px; top: 477px;
    font-weight: 700; font-style: italic;
    font-size: 47px; line-height: 53px; text-align: center;
    letter-spacing: -0.3px;
    color: var(--ink);
  }
  .tagline__name { color: var(--red); }

  .brand {
    position: absolute; left: 532px; top: 6px;
    display: flex; align-items: flex-start;
  }
  .brand__mark {
    width: 203px; height: 203px;
    border: 3px solid var(--red); padding: 6px;
  }
  .brand__mark span { display: block; width: 100%; height: 100%; background: var(--red); }
  .brand__name {
    margin-left: 26px; margin-top: 2px;
    font-family: "Oswald", "Arial Narrow", sans-serif;
    font-weight: 500; color: var(--ink);
    text-transform: uppercase;
  }
  .brand__name-main { display: block; font-size: 150px; line-height: 150px; letter-spacing: 2px; }
  .brand__name-sub { display: block; font-size: 44px; line-height: 50px; letter-spacing: 0.5px; }

  .profile {
    position: absolute; right: 31px; top: 222px; text-align: right;
  }
  .profile__name { color: var(--red); font-weight: 700; font-size: 46px; line-height: 50px; }
  .profile__role { font-style: italic; font-size: 20px; line-height: 24px; }

  .details {
    position: absolute; left: 527px; top: 306px; width: 560px;
  }
  .details__headline {
    color: var(--red); font-weight: 700; font-size: 32.5px; line-height: 38px;
    margin-bottom: 12px; white-space: nowrap;
  }
  .strengths { list-style: none; font-size: 21px; line-height: 27px; width: 562px; }
  .strengths li { position: relative; padding-left: 16px; }
  .strengths li::before {
    content: ""; position: absolute; left: 2px; top: 12px;
    width: 5px; height: 5px; border-radius: 50%; background: var(--red);
  }
  .qualifications {
    margin-top: 11px; width: 555px; font-size: 19.5px; line-height: 24.5px;
  }
  .qualifications__label { color: var(--red); font-weight: 700; }
</style>
</head>
<body>
<main class="flyer">
  <div class="flyer__frame">
    <svg class="crowd-art" viewBox="0 0 520 689" role="img" aria-label="Illustration of a group of business people in suits walking forward in silhouette, reflected on a glossy floor">
      <defs>
        <linearGradient id="crowdTone" x1="0" y1="0" x2="0" y2="1">
          <stop offset="0" stop-color="var(--figure-light)" stop-opacity="0.35"/>
          <stop offset="0.15" stop-color="var(--figure-mid)" stop-opacity="0.75"/>
          <stop offset="0.55" stop-color="var(--figure-mid)" stop-opacity="0.65"/>
          <stop offset="0.75" stop-color="var(--figure-light)" stop-opacity="0.35"/>
          <stop offset="0.95" stop-color="#ffffff" stop-opacity="0"/>
        </linearGradient>
        <radialGradient id="crowdCore" cx="0.5" cy="0.38" r="0.5">
          <stop offset="0" stop-color="var(--figure-dark)" stop-opacity="0.85"/>
          <stop offset="0.6" stop-color="var(--figure-dark)" stop-opacity="0.35"/>
          <stop offset="1" stop-color="var(--figure-dark)" stop-opacity="0"/>
        </radialGradient>
        <linearGradient id="edgeFade" x1="0" y1="0" x2="1" y2="0">
          <stop offset="0" stop-color="#fff" stop-opacity="0.6"/>
          <stop offset="0.12" stop-color="#fff" stop-opacity="1"/>
          <stop offset="0.85" stop-color="#fff" stop-opacity="1"/>
          <stop offset="1" stop-color="#fff" stop-opacity="0"/>
        </linearGradient>
        <mask id="edgeMask">
          <rect x="0" y="0" width="520" height="689" fill="url(#edgeFade)"/>
        </mask>
      </defs>
      <g mask="url(#edgeMask)">
        <rect x="0" y="0" width="520" height="689" fill="url(#crowdTone)"/>
        <ellipse cx="255" cy="250" rx="230" ry="300" fill="url(#crowdCore)"/>
      </g>
    </svg>

    <p class="tagline">Need a bi-lingual and<br>b-cultural expert?<br>Meet <span class="tagline__name">Colin Marsh</span>!</p>

    <div class="brand">
      <div class="brand__mark"><span></span></div>
      <p class="brand__name">
        <span class="brand__name-main">LUPE</span>
        <span class="brand__name-sub">Advisory Group</span>
      </p>
    </div>

    <div class="profile">
      <h1 class="profile__name">Colin Marsh</h1>
      <p class="profile__role">Senior Consultant and Director</p>
    </div>

    <section class="details">
      <h2 class="details__headline">Expert on all matters China related</h2>
      <ul class="strengths">
        <li>Writes and speak fluently in Chinese</li>
        <li>Expert in Australia/China Business relations</li>
        <li>Bi-cultural expert &nbsp;from Australian and Chinese history, art, food and more, Colin Marsh provides his clients with more than translation services.</li>
      </ul>
      <p class="qualifications"><span class="qualifications__label">Qualifications:</span> Bachelor of Arts (Asian Studies), Bachelor of Business (Applied Economics – International Trade), Master of Business in Applied Economics (International Business) and currently completing a Doctor of Business Administration (International Business Management) which has an economics focus and researches the export of Australian professional services to China.</p>
    </section>
  </div>
</main>
</body>
</html>
```